Sleek, Professional Business Card Design Needed

Business Cards - Logo Attached.

We are a solar consulting company. We are national and want our cards to represent the professional high quality products that we offer.

Industry/Entity Type

Business

Contact Information for Business Card

n/a

Requirements
Must have
• Design
• Name
• Position
• Number
• Email
• Address
Should not have
• Not be too crowded

```html
<!DOCTYPE html>
<html lang="en">
<head>
<meta charset="utf-8">
<title>Solvane Energy Business Card</title>
<link rel="stylesheet" href="https://fonts.googleapis.com/css2?family=Montserrat:wght@200;300;400;600;700;800&display=swap">
<style>
  :root {
    --canvas: #e9e7e4;
    --card: #222222;
    --blue: #1b8fd0;
    --green: #8cc63f;
    --white: #ffffff;
    --title-blue: #2f6f9c;
  }
  * { margin: 0; padding: 0; box-sizing: border-box; }
  html, body {
    width: 1200px; height: 1200px; overflow: hidden;
    background: var(--canvas);
    font-family: "Montserrat", sans-serif;
  }
  .canvas {
    position: relative; width: 1200px; height: 1200px;
    display: flex; flex-direction: column; align-items: center; justify-content: center;
    gap: 60px;
  }
  .card {
    position: relative;
    width: 700px; height: 400px;
    background: var(--card);
    border-radius: 4px;
    box-shadow: 0 10px 30px rgba(0,0,0,0.18);
    overflow: hidden;
  }
  .card--front {
    display: flex; align-items: center; justify-content: center; gap: 18px;
  }
  .brand-dot {
    width: 34px; height: 34px; border-radius: 50%;
    background: var(--green);
  }
  .brand-name {
    color: var(--blue);
    font-weight: 700;
    font-size: 40px;
    letter-spacing: 2px;
    text-transform: uppercase;
  }
  .card--back .brand-name {
    position: absolute; top: 90px; left: 0; right: 0;
    text-align: center;
    font-size: 52px;
  }
  .holder {
    position: absolute; left: 70px; top: 250px; width: 260px; text-align: right;
  }
  .holder__name {
    color: var(--white); font-weight: 800; font-size: 22px;
  }
  .holder__title {
    color: var(--title-blue); font-weight: 200; font-size: 22px; margin-top: 10px;
  }
  .divider {
    position: absolute; left: 360px; top: 240px;
    width: 4px; height: 120px; background: var(--white);
  }
  .contact {
    position: absolute; left: 390px; top: 246px;
    font-size: 17px; line-height: 22px; font-weight: 400;
    color: var(--white);
  }
  .contact__link { color: var(--blue); display: block; }
</style>
</head>
<body>
<main class="canvas">
  <section class="card card--front" aria-label="Card front">
    <span class="brand-dot"></span>
    <span class="brand-name">Solvane Energy</span>
  </section>

  <section class="card card--back" aria-label="Card back">
    <div class="brand-name">Solvane Energy</div>
    <div class="holder">
      <p class="holder__name">Name Firstname</p>
      <p class="holder__title">Title</p>
    </div>
    <span class="divider"></span>
    <address class="contact" style="font-style:normal">
      Brightmere inc<br>
      48E 19 Street<br>
      Address NY10003<br>
      <span class="contact__link">info@solvane.com</span>
      <span class="contact__link">www.solvane.com</span>
    </address>
  </section>
</main>
</body>
</html>
```